A design led business card for the construction industry

High-end business card to match logo. White logo on dark grey/off black to the front. Matching dark font on white to back, possibly with logo design again.

We offer construction and project management services to commercial and private clients in the UK. Projetcs range from newbuilds, conversion of listed buildings and refurbishments and extensions of existing homes. Our focus is on quality and attention to detail using the highest skills.

Contact Information for Business Card

Name; Dorian Hatch BSc
Position; Project Manager
Mobile; 07962 804 157
Tel; 01632 958412
email; dorian@framelark.co.uk
web; www.framelark.co.uk
Address; Ashby Wendle, KT4 7PZ

Colors

Designer to choose only greyscale colors for use in the design.

Requirements
Must have
• To include the below description of the business,

CONSTRUCTION - PROJECT MANAGEMENT
Nice to have
• The posibility of the top back of the card being used as a ruler. So will have a measurement to scale in mm or an architect scale of 1:50
Should not have
• Should not be portrait

```html
<!DOCTYPE html>
<html lang="en">
<head>
<meta charset="utf-8">
<title>Framelark business card</title>
<link href="https://fonts.googleapis.com/css2?family=Roboto:wght@300;400;500;700&display=swap" rel="stylesheet">
<style>
  :root {
    --stage: #1c1c1c;
    --card-dark: #262626;
    --card-light: #f7f7f7;
    --ink-dark: #1a1a1a;
    --ink-mid: #333333;
    --ink-light: #ffffff;
    --rule-grey: #bdbdbd;
    --faint-grey: #e4e4e4;
  }
  * { margin: 0; padding: 0; box-sizing: border-box; }
  html, body {
    width: 1200px; height: 900px; overflow: hidden;
    background: var(--stage);
    font-family: "Roboto", Arial, sans-serif;
  }
  .stage { position: relative; width: 1200px; height: 900px; }
  .card {
    position: absolute; left: 250px; width: 700px; height: 400px;
    overflow: hidden; border-radius: 3px;
    box-shadow: 0 18px 40px rgba(0,0,0,.55);
  }
  /* front */
  .card-front { top: 40px; background: var(--card-dark); }
  .ruler { position: absolute; left: 0; top: 0; width: 700px; height: 70px; }
  .ruler text { fill: var(--ink-light); font-family: "Roboto", Arial, sans-serif; font-size: 13px; font-weight: 300; }
  .pattern-field {
    position: absolute; left: 30px; top: 80px; width: 640px; height: 300px;
    background: radial-gradient(ellipse at 70% 40%, rgba(255,255,255,.09), rgba(255,255,255,.02) 70%);
    border-radius: 4px;
  }
  .front-brand {
    position: absolute; left: 0; top: 200px; width: 700px;
    display: flex; align-items: center; justify-content: center; gap: 18px;
  }
  .brand-square { width: 46px; height: 46px; border: 2px solid var(--ink-light); }
  .brand-name {
    font-weight: 300; font-size: 24px; letter-spacing: 9px; color: var(--ink-light);
  }
  /* back */
  .card-back { top: 470px; background: linear-gradient(135deg, #ffffff, #ececec); }
  .back-decoration {
    position: absolute; left: 330px; top: -20px; width: 420px; height: 380px;
    background: linear-gradient(160deg, rgba(0,0,0,.07), rgba(0,0,0,.03));
    border-radius: 14px;
  }
  .back-brand {
    position: absolute; left: 70px; top: 150px; width: 200px;
    display: flex; flex-direction: column; align-items: center; gap: 14px;
  }
  .back-brand .brand-square { width: 70px; height: 70px; border: 3px solid var(--ink-dark); }
  .back-brand .brand-name { color: var(--ink-dark); font-size: 16px; letter-spacing: 7px; }
  .contact-block { position: absolute; left: 400px; top: 95px; width: 260px; color: var(--ink-dark); }
  .person-name { font-size: 22px; font-weight: 700; letter-spacing: .5px; }
  .person-role { font-size: 13px; font-weight: 500; margin-top: 3px; color: var(--ink-mid); }
  .divider { height: 1px; background: var(--ink-dark); margin: 14px 0 16px; width: 240px; }
  .contact-list { list-style: none; }
  .contact-list li {
    display: flex; align-items: center; gap: 12px;
    font-size: 13.5px; font-weight: 400; height: 27px;
  }
  .contact-list svg { width: 15px; height: 15px; flex: none; }
</style>
</head>
<body>
<main class="stage">

  <section class="card card-front" aria-label="Card front">
    <svg class="ruler" viewBox="0 0 700 70" aria-label="Centimetre ruler">
      <g stroke="#ffffff" stroke-width="1.4">
        <!-- cm ticks -->
        <line x1="40" y1="0" x2="40" y2="22"/><line x1="102" y1="0" x2="102" y2="22"/>
        <line x1="164" y1="0" x2="164" y2="22"/><line x1="226" y1="0" x2="226" y2="22"/>
        <line x1="288" y1="0" x2="288" y2="22"/><line x1="350" y1="0" x2="350" y2="22"/>
        <line x1="412" y1="0" x2="412" y2="22"/><line x1="474" y1="0" x2="474" y2="22"/>
        <line x1="536" y1="0" x2="536" y2="22"/><line x1="598" y1="0" x2="598" y2="22"/>
        <line x1="660" y1="0" x2="660" y2="22"/>
        <!-- half cm ticks -->
        <line x1="71" y1="0" x2="71" y2="13"/><line x1="133" y1="0" x2="133" y2="13"/>
        <line x1="195" y1="0" x2="195" y2="13"/><line x1="257" y1="0" x2="257" y2="13"/>
        <line x1="319" y1="0" x2="319" y2="13"/><line x1="381" y1="0" x2="381" y2="13"/>
        <line x1="443" y1="0" x2="443" y2="13"/><line x1="505" y1="0" x2="505" y2="13"/>
        <line x1="567" y1="0" x2="567" y2="13"/><line x1="629" y1="0" x2="629" y2="13"/>
      </g>
      <g text-anchor="middle">
        <text x="40" y="40">0</text><text x="102" y="40">1</text><text x="164" y="40">2</text>
        <text x="226" y="40">3</text><text x="288" y="40">4</text><text x="350" y="40">5</text>
        <text x="412" y="40">6</text><text x="474" y="40">7</text><text x="536" y="40">8</text>
        <text x="598" y="40">9</text><text x="660" y="40">10</text>
      </g>
    </svg>
    <div class="pattern-field" role="img" aria-label="Faint repeated pattern of outlined brand squares fading across the dark card"></div>
    <div class="front-brand">
      <span class="brand-square"></span>
      <span class="brand-name">FRAMELARK</span>
    </div>
  </section>

  <section class="card card-back" aria-label="Card back">
    <div class="back-decoration" role="img" aria-label="Large faint light grey brand decoration behind the contact details"></div>
    <div class="back-brand">
      <span class="brand-square"></span>
      <span class="brand-name">FRAMELARK</span>
    </div>
    <div class="contact-block">
      <h1 class="person-name">DORIAN HATCH BSC</h1>
      <p class="person-role">Project Manager</p>
      <div class="divider"></div>
      <ul class="contact-list">
        <li><svg viewBox="0 0 16 16"><rect x="4" y="1" width="8" height="14" rx="1.5" fill="none" stroke="#1a1a1a" stroke-width="1.5"/><line x1="6.5" y1="12.5" x2="9.5" y2="12.5" stroke="#1a1a1a" stroke-width="1.2"/></svg>07962 804 157</li>
        <li><svg viewBox="0 0 16 16"><path d="M4 1.5 L6.5 4.5 L5 6.5 C6 8.5 7.5 10 9.5 11 L11.5 9.5 L14.5 12 L12.5 14.5 C7 14 2 9 1.5 3.5 Z" fill="#1a1a1a"/></svg>01632 958412</li>
        <li><svg viewBox="0 0 16 16" fill="none" stroke="#1a1a1a" stroke-width="1.3"><circle cx="8" cy="8" r="6.5"/><ellipse cx="8" cy="8" rx="2.8" ry="6.5"/><line x1="1.5" y1="8" x2="14.5" y2="8"/></svg>www.framelark.co.uk</li>
        <li><svg viewBox="0 0 16 16"><rect x="1" y="3" width="14" height="10" fill="#1a1a1a"/><path d="M1 3 L8 9 L15 3" fill="none" stroke="#f7f7f7" stroke-width="1.2"/></svg>dorian@framelark.co.uk</li>
        <li><svg viewBox="0 0 16 16"><path d="M8 15 C4 10 3 8 3 6 A5 5 0 0 1 13 6 C13 8 12 10 8 15 Z" fill="#1a1a1a"/><circle cx="8" cy="6" r="1.8" fill="#f7f7f7"/></svg>Ashby Wendle, KT4 7PZ</li>
      </ul>
    </div>
  </section>

</main>
</body>
</html>
```